Tamblin Gardening Fresh New Website

We are looking to create a simple fresh website for our landscaping business. The website should appeal to a 'high end' audience. We deal with a lot of Embassies and affluent clients who have extremely large gardens that are meticulously maintained. The site is about communicating our excellent landscaping and customer service skills and encouraging new clients to reach out and engage us to take care of their gardens.

The website is basically going to be our business card, it will have almost no functionality other than two 'contact us' forms, one for smaller clients and one for more detailed projects.

The website will not have a lot of written content and will have to show photos of beautifully landscaped gardens.

The main logo in black will influence the site, however, we are open to all suggestions.

We are expecting to have the following pages:
Home Page
Services
About Us
Contact Us
Showcase (photo gallery of our work)

We need someone who can code it to wordpress and be available for minor changes over a number of days. They will be simple tweaks.

```html
<!DOCTYPE html>
<html lang="en">
<head>
<meta charset="utf-8">
<title>Tamblin Gardening – Home Page</title>
<link href="https://fonts.googleapis.com/css2?family=Tinos:wght@400;700&family=Roboto:wght@400;500;700&display=swap" rel="stylesheet">
<style>
:root{
  --board:#f5fce9;
  --green:#1e8f2a;
  --btn:#3cb043;
  --lime:#8cc63f;
  --deep:#0d7a1c;
  --ink:#222;
  --soft:#f8f9f6;
  --line:#e6eadf;
}
*{box-sizing:border-box;margin:0;padding:0}
html,body{width:1200px;height:3125px;overflow:hidden}
body{background:var(--board);font-family:'Roboto',sans-serif;color:var(--ink);position:relative}
.abs{position:absolute}

.board-brand{position:absolute;top:80px;width:100%;display:flex;justify-content:center;align-items:center;gap:8px;font-family:'Tinos',serif;font-size:20px;color:var(--green)}
.board-brand i{width:12px;height:12px;border-radius:50%;background:var(--green);display:block}
.board-title{position:absolute;top:132px;width:100%;text-align:center;font-family:'Tinos',serif;font-weight:700;font-size:54px;color:var(--green)}
.board-sub{position:absolute;top:198px;width:100%;text-align:center;font-family:'Tinos',serif;font-size:38px;color:var(--green)}
.board-thanks{position:absolute;top:3038px;width:100%;text-align:center;font-family:'Tinos',serif;font-weight:700;font-size:40px;color:var(--green)}

.page{position:absolute;left:277px;top:268px;width:648px;height:2718px;background:#fff;overflow:hidden;box-shadow:0 10px 40px rgba(60,120,30,.12)}
.photo{position:absolute;overflow:hidden}

.hero{left:0;top:0;width:648px;height:317px;background:linear-gradient(180deg,#6d9ad0 0%,#9cbcd9 22%,#4f7a3a 45%,#2f5a22 70%,#4e7a35 100%)}
.hero-shade{position:absolute;inset:0;background:rgba(0,0,0,.22)}
.nav{position:absolute;top:22px;left:0;width:648px;display:flex;justify-content:center;align-items:center;gap:24px;color:#fff;font-family:'Tinos',serif;font-size:6.5px}
.nav .brand{font-size:7px;margin:0 22px}
.hero-copy{position:absolute;top:96px;width:648px;text-align:center;color:#fff}
.hero-copy .welcome{font-family:'Tinos',serif;font-size:12px}
.hero-copy h1{font-family:'Tinos',serif;font-weight:700;font-size:27px;margin-top:4px;line-height:1}
.hero-copy .tag{font-family:'Tinos',serif;font-size:18px;margin-top:5px}
.hero-copy .small{font-size:6.5px;margin-top:10px}
.btn-white{position:absolute;left:281px;top:195px;width:86px;height:19px;background:#fff;border-radius:3px;font-size:6px;color:var(--green);font-weight:500;display:flex;align-items:center;justify-content:center}

.consult{position:absolute;left:377px;top:290px;width:177px;height:262px;background:#fff;border-radius:6px;box-shadow:0 6px 24px rgba(0,0,0,.08)}
.consult h3{position:absolute;left:16px;top:18px;font-size:9.5px;font-weight:500;color:var(--green);display:flex;align-items:center;gap:6px}
.dot-ico{width:8px;height:8px;border-radius:50%;background:var(--btn);display:inline-block;flex:none}
.field{position:absolute;left:16px;width:145px;height:22px;background:var(--soft);border-radius:3px;font-size:5.5px;color:#999;padding:7px 10px}
.field .caret{position:absolute;right:10px;top:7px;color:var(--green);font-size:6px}
.btn-green{position:absolute;background:var(--btn);color:#fff;border-radius:3px;font-size:5.5px;font-weight:500;display:flex;align-items:center;justify-content:center}
.btn-outline{position:absolute;background:#fff;border:1px solid var(--line);border-radius:3px;font-size:5.5px;color:var(--green);font-weight:500;display:flex;align-items:center;justify-content:center;white-space:nowrap}

.intro{position:absolute;left:93px;top:362px;width:260px}
.intro h2{font-family:'Tinos',serif;font-weight:400;font-size:17px;line-height:23px;color:var(--deep)}
.intro h2 b{font-weight:700}
.intro p{font-size:6px;line-height:11px;color:#444;margin-top:12px}
.intro p span{color:var(--green)}
.ticks{margin-top:12px;list-style:none}
.ticks li{font-size:6.8px;color:var(--green);font-weight:500;display:flex;align-items:center;gap:8px;height:17px}

.section-label{position:absolute;width:648px;text-align:center;font-size:5.8px;letter-spacing:.5px;color:var(--lime)}
.section-label i{display:block;margin:0 auto 4px;width:7px;height:7px;border-radius:50%;background:var(--lime)}
.section-title{position:absolute;width:648px;text-align:center;font-family:'Tinos',serif;font-size:17px;color:var(--deep)}

.filters{position:absolute;top:746px;left:93px;width:462px;display:flex;justify-content:space-between;padding:0 42px 0 50px;font-family:'Tinos',serif;font-size:6px;color:#777}
.filters .on{color:var(--green)}
.work{width:147px;height:111px;border:1px solid #ddd}
.work-card{position:absolute;left:251px;top:897px;width:147px;height:111px;background:#fff;border:2px solid #cfe7c6;box-shadow:0 4px 12px rgba(0,0,0,.1);text-align:center;padding-top:16px}
.work-card h4{font-size:7.5px;font-weight:500}
.work-card p{font-size:5px;color:#777;line-height:7px;margin:6px 14px 0}
.work-card .keys{font-size:5px;color:#555;line-height:10px;margin-top:6px}
.work-card .view{font-size:5.5px;color:var(--green);margin-top:8px}

.review{position:absolute;top:1154px;width:147px;height:82px;background:#fff;border-radius:4px;box-shadow:0 3px 14px rgba(0,0,0,.07);text-align:center;padding:28px 14px 0}
.avatar{position:absolute;top:-8px;left:62px;width:23px;height:23px;border-radius:50%;background:linear-gradient(#b9bcc0,#6b6f74)}
.review .who{font-family:'Tinos',serif;font-size:6px}
.review .txt{font-size:5px;line-height:7px;color:#777;margin-top:4px}
.review .stars{font-size:6.5px;color:#f29b1d;letter-spacing:1px;margin-top:5px}
.slider-dots{position:absolute;top:1248px;left:309px;display:flex;gap:3px}
.slider-dots span{width:8px;height:2px;background:#c8e0bf}
.slider-dots span.on{background:var(--btn)}

.services-band{position:absolute;left:0;top:1346px;width:648px;height:590px;background:var(--soft)}
.svc-title{position:absolute;font-family:'Tinos',serif;font-size:12.5px;line-height:16px;color:var(--deep)}
.svc-text{position:absolute;font-size:5.8px;line-height:9px;color:#333}
.frame{position:absolute;background:#fff;border-radius:18px}

.about-label{position:absolute;left:367px;top:1990px;font-size:5.8px;color:var(--lime);display:flex;align-items:center;gap:5px}
.about-title{position:absolute;left:367px;top:2007px;font-family:'Tinos',serif;font-size:19px;line-height:23px;color:var(--deep)}
.about-text{position:absolute;left:367px;top:2057px;width:190px;font-size:5.8px;line-height:10px;color:#333}
.about-text span{color:var(--green)}
.stat{position:absolute;top:2192px}
.stat b{display:block;font-family:'Tinos',serif;font-weight:400;font-size:16px;color:var(--green)}
.stat small{display:block;font-size:5.5px;color:#777;margin-top:2px}
.play{position:absolute;left:388px;top:2170px;width:32px;height:32px;border-radius:50%;background:rgba(255,255,255,.35)}

.cta-wave{position:absolute;left:0;top:2290px;width:648px;height:355px}
.cta-form{position:absolute;left:93px;top:2407px;width:265px;height:200px;border:1px solid rgba(255,255,255,.3);background:rgba(255,255,255,.06);border-radius:6px;color:#fff}
.cta-form h3{position:absolute;left:14px;top:18px;font-family:'Tinos',serif;font-weight:400;font-size:12.5px;line-height:15px}
.line-field{position:absolute;height:16px;border-bottom:1px solid rgba(255,255,255,.45);font-size:5px;color:rgba(255,255,255,.85)}
.cta-label{position:absolute;left:383px;top:2430px;font-size:5.5px;color:#fff;display:flex;align-items:center;gap:5px;white-space:nowrap}
.cta-h{position:absolute;left:383px;top:2447px;font-family:'Tinos',serif;font-size:18px;line-height:24px;color:#fff}
.contact-row{position:absolute;left:383px;display:flex;align-items:center;gap:10px;color:#fff;font-size:7px;line-height:11px}
.contact-row .ico{width:22px;height:22px;border-radius:50%;background:#fff;display:flex;align-items:center;justify-content:center;flex:none}

.footer{position:absolute;left:0;top:2645px;width:648px;height:54px;background:var(--lime)}
.footer .brand{position:absolute;left:93px;top:22px;font-family:'Tinos',serif;color:#fff;font-size:8px}
.footer nav{position:absolute;left:226px;top:24px;display:flex;gap:22px;font-family:'Tinos',serif;font-size:6px;color:#fff}
.social{position:absolute;top:16px;width:22px;height:22px;border-radius:50%;background:#fff}
.to-top{position:absolute;left:598px;top:2630px;width:31px;height:31px;border-radius:50%;background:#fff;box-shadow:0 3px 10px rgba(0,0,0,.15);display:flex;align-items:center;justify-content:center}
.bottom-bar{position:absolute;left:0;top:2699px;width:648px;height:19px;background:var(--deep);font-size:5px;color:#dfe;display:flex;justify-content:space-between;align-items:center;padding:0 93px}
</style>
</head>
<body>

<div class="board-brand"><i></i>Tamblin Gardening</div>
<div class="board-title">TAMBLIN GARDENING</div>
<div class="board-sub">Home Page</div>

<main class="page">
  <section class="photo hero" role="img" aria-label="Landscaped estate garden with lawns, sculpted shrubs and evergreen trees under a blue sky">
    <div class="hero-shade"></div>
  </section>
  <nav class="nav"><span>SERVICE</span><span>ABOUT US</span><span class="brand">Tamblin Gardening</span><span>GALLERY</span><span>CONTACT US</span></nav>
  <div class="hero-copy">
    <div class="welcome">WELCOME TO</div>
    <h1>TAMBLIN GARDENING</h1>
    <div class="tag">Where Gardens Come to Life</div>
    <div class="small">Transforming Ordinary Spaces into Extraordinary Masterpieces.</div>
  </div>
  <div class="btn-white">Get a Quote&nbsp;→</div>

  <div class="intro">
    <h2><b>Indutry- Leading</b> Expertise &amp;<br>Consistent Customer Satisfaction</h2>
    <p>Welcome to <span>Tamblin Gardening</span>, where the artistry of nature meets the craftsmanship of our passion. Our journey began with a simple love for the great outdoors, a desire to transform ordinary landscapes into extraordinary masterpieces, and a commitment to creating outdoor sanctuaries that transcend the ordinary.</p>
    <ul class="ticks">
      <li><span class="dot-ico"></span>Unparalleled attention to detail.</li>
      <li><span class="dot-ico"></span>Bespoke designs tailored to your lifestyle.</li>
      <li><span class="dot-ico"></span>Exquisite craftsmanship and quality materials.</li>
    </ul>
  </div>
  <div class="btn-outline" style="left:93px;top:530px;width:80px;height:20px">Get a Quote&nbsp;→</div>

  <div class="consult">
    <h3><span class="dot-ico"></span>Schedule a Consultation</h3>
    <div class="field" style="top:40px">Your Name</div>
    <div class="field" style="top:72px">Your Email</div>
    <div class="field" style="top:104px">Landscape Maintenance<span class="caret">▼</span></div>
    <div class="field" style="top:136px;height:58px">Message</div>
    <div class="btn-green" style="left:63px;top:226px;width:98px;height:19px">Request a Quote&nbsp;→</div>
  </div>

  <div class="section-label" style="top:688px"><i></i>PORTFOLIO</div>
  <div class="section-title" style="top:711px">Our Past Projects</div>
  <div class="filters"><span class="on">All</span><span>Landscape</span><span>Gardens</span><span>Outdoor Living Space</span><span>Architectural</span></div>

  <div class="photo work" style="left:93px;top:774px;background:linear-gradient(180deg,#5b94d6 0%,#9cc4e6 40%,#6a9b48 60%,#b04c8a 75%,#7d8a70 100%)" role="img" aria-label="Public garden with flower beds under a blue sky"></div>
  <div class="photo work" style="left:251px;top:774px;background:linear-gradient(180deg,#4c6b3b 0%,#6e8c55 35%,#d0407a 55%,#f0cf22 75%,#b8b09a 100%)" role="img" aria-label="Formal garden path lined with yellow and pink flowers"></div>
  <div class="photo work" style="left:407px;top:774px;background:linear-gradient(180deg,#7fb3e3 0%,#6fae3c 35%,#d63b8c 60%,#78b93a 100%)" role="img" aria-label="Lakeside garden with pink flowering shrubs"></div>
  <div class="photo work" style="left:93px;top:897px;background:linear-gradient(180deg,#8eae6c 0%,#557c33 40%,#3f7a2a 70%,#66a33a 100%)" role="img" aria-label="Sunlit park with tall trees and winding path"></div>
  <div class="work-card">
    <h4>OUTDOOR LIVING SPACE</h4>
    <p>Transforming Ordinary Spaces into Extraordinary Masterpieces</p>
    <div class="keys">KEY DESIGN ELEMENTS<br>KEY DESIGN ELEMENTS</div>
    <div class="view">View Work&nbsp;→</div>
  </div>
  <div class="photo work" style="left:407px;top:897px;background:linear-gradient(135deg,#5e8a3c 0%,#b83d8e 45%,#d35aa5 65%,#6d8a4d 100%)" role="img" aria-label="Stone garden steps among blooming azaleas"></div>
  <div class="btn-outline" style="left:276px;top:1020px;width:94px;height:20px">View All Works&nbsp;→</div>

  <div class="section-label" style="top:1090px"><i></i>TESTIMONIALS</div>
  <div class="section-title" style="top:1111px">What People Say About Us</div>
  <div class="review" style="left:93px"><div class="avatar" role="img" aria-label="Client portrait"></div><div class="who">Maren Holt</div><div class="txt">Lorem ipsum dolor sit amet consectetur. Est vestibulum eros purus commodo vitae vitae facilisis.</div><div class="stars">★★★★☆</div></div>
  <div class="review" style="left:251px"><div class="avatar" role="img" aria-label="Client portrait"></div><div class="who">Ines Varga</div><div class="txt">Lorem ipsum dolor sit amet consectetur. Est vestibulum eros purus commodo vitae vitae facilisis.</div><div class="stars">★★★★★</div></div>
  <div class="review" style="left:407px"><div class="avatar" role="img" aria-label="Client portrait"></div><div class="who">Tomas Reyes</div><div class="txt">Lorem ipsum dolor sit amet consectetur. Est vestibulum eros purus commodo vitae vitae facilisis.</div><div class="stars">★★★★★</div></div>
  <div class="slider-dots"><span class="on"></span><span></span><span></span></div>

  <div class="services-band"></div>
  <div class="section-label" style="top:1386px"><i></i>SERVICES</div>
  <div class="section-title" style="top:1409px">Elevate Your Outdoor Living Experience</div>

  <div class="photo" style="left:93px;top:1443px;width:286px;height:218px;border-radius:4px 4px 4px 12px;background:linear-gradient(160deg,#a9c96a 0%,#4f8a2c 35%,#2e5e22 60%,#6c7a66 80%,#3f6a2a 100%)" role="img" aria-label="Wooden boardwalk through lush green garden"></div>
  <div class="svc-title" style="left:396px;top:1489px">Custom Garden Design &amp;<br>Installation</div>
  <div class="svc-text" style="left:396px;top:1529px;width:160px">Lorem ipsum dolor sit amet consectetur. Est vestibulum eros purus commodo vitae vitae facilisis.</div>
  <div class="btn-green" style="left:396px;top:1563px;width:99px;height:19px">Request a Quote&nbsp;→</div>

  <div class="frame" style="left:258px;top:1625px;width:296px;height:235px"></div>
  <div class="photo" style="left:267px;top:1634px;width:287px;height:221px;border-radius:12px 4px 12px 4px;background:linear-gradient(150deg,#6aa03a 0%,#d2427f 25%,#4f9a3a 45%,#3aa8b0 60%,#5d9232 80%,#b9d77c 100%)" role="img" aria-label="Gardener tending flowering plants in a nursery"></div>
  <div class="svc-title" style="left:93px;top:1726px">Seasonal<br>Maintenance &amp; Care</div>
  <div class="svc-text" style="left:93px;top:1766px;width:160px">Lorem ipsum dolor sit amet consectetur. Est vestibulum eros purus commodo vitae vitae facilisis.</div>
  <div class="btn-green" style="left:93px;top:1799px;width:99px;height:19px">Request a Quote&nbsp;→</div>
  <div class="btn-outline" style="left:247px;top:1872px;width:151px;height:19px">Discover Our Full Range of Services&nbsp;→</div>

  <div class="photo" style="left:93px;top:1979px;width:246px;height:198px;background:linear-gradient(150deg,#56803a 0%,#7da74a 30%,#e2722a 50%,#4b7d2e 70%,#a2b850 100%)" role="img" aria-label="Gardener in orange uniform planting shrubs"></div>
  <div class="about-label"><span class="dot-ico" style="width:6px;height:6px"></span>ABOUT US</div>
  <div class="about-title">We have Expertise in all<br>of Garden Maintenance</div>
  <div class="about-text">Welcome to <span>Tamblin Gardening</span>, where nature's artistry meets our passion for perfection. Founded by [Founder's Name], our journey began with a simple love for the outdoors and a commitment to crafting extraordinary landscapes.</div>
  <div class="frame" style="left:310px;top:2114px;width:192px;height:158px"></div>
  <div class="photo" style="left:321px;top:2122px;width:181px;height:140px;background:linear-gradient(180deg,#b9cfe0 0%,#6b8e4e 35%,#3d6b3a 60%,#7a9a62 100%)" role="img" aria-label="Water garden with lily pads and surrounding trees"></div>
  <div class="play"></div>
  <svg class="abs" style="left:398px;top:2179px" width="14" height="14" aria-hidden="true"><path d="M2 1 L13 7 L2 13 Z" fill="#3cb043"/></svg>
  <div class="stat" style="left:93px"><b>550+</b><small>PROJECTS DONE</small></div>
  <div class="stat" style="left:159px"><b>100+</b><small>PROFESSIONAL TEAM</small></div>
  <div class="stat" style="left:240px"><b>99%</b><small>HAPPY CUSTOMERS</small></div>

  <svg class="cta-wave" viewBox="0 0 648 355" preserveAspectRatio="none" aria-hidden="true">
    <defs><linearGradient id="ctaGrad" x1="0" y1="0" x2="0" y2="1"><stop offset="0" stop-color="#1fb92c"/><stop offset="1" stop-color="#0d7a1c"/></linearGradient></defs>
    <path d="M0 20 C40 0 80 50 130 55 S200 20 250 10 S320 60 360 50 S440 10 480 20 S560 120 600 90 S640 40 648 40 L648 355 L0 355 Z" fill="url(#ctaGrad)"/>
  </svg>
  <div class="cta-form">
    <h3>Transform your outdoor oasis with<br>Tamblin Gardening</h3>
    <div class="line-field" style="left:14px;top:60px;width:105px">First Name*</div>
    <div class="line-field" style="left:146px;top:60px;width:105px">Last Name*</div>
    <div class="line-field" style="left:14px;top:82px;width:105px">Email*</div>
    <div class="line-field" style="left:146px;top:82px;width:105px">Phone Number*</div>
    <div class="line-field" style="left:14px;top:104px;width:237px;height:40px">Your Message Here</div>
    <div class="abs" style="left:14px;top:166px;font-size:4.5px">By subscribing, you agree to our Privacy Policy.*</div>
    <div class="btn-outline" style="left:131px;top:160px;width:120px;height:19px">Schedule a Consultation&nbsp;→</div>
  </div>
  <div class="cta-label"><span class="dot-ico" style="width:6px;height:6px;background:#bfe59c"></span>READY TO GET STARTED</div>
  <div class="cta-h">Let's Talk<br>About Your Project.</div>
  <div class="contact-row" style="top:2505px"><span class="ico"><svg width="10" height="10" viewBox="0 0 24 24"><path d="M6.6 10.8a15 15 0 006.6 6.6l2.2-2.2c.3-.3.7-.4 1-.2 1.1.4 2.3.6 3.6.6.6 0 1 .4 1 1V20c0 .6-.4 1-1 1A17 17 0 013 4c0-.6.4-1 1-1h3.5c.6 0 1 .4 1 1 0 1.3.2 2.5.6 3.6.1.3 0 .7-.2 1z" fill="#1e8f2a"/></svg></span>+110 4471 902</div>
  <div class="contact-row" style="top:2530px"><span class="ico"><svg width="10" height="10" viewBox="0 0 24 24"><path d="M12 2a7 7 0 00-7 7c0 5 7 13 7 13s7-8 7-13a7 7 0 00-7-7zm0 9.5A2.5 2.5 0 1112 6a2.5 2.5 0 010 5.5z" fill="#1e8f2a"/></svg></span>418 Orchard Lane, Fernbrook,<br>Ohio 40217</div>
  <div class="contact-row" style="top:2564px"><span class="ico"><svg width="10" height="10" viewBox="0 0 24 24"><path d="M3 5h18v14H3z" fill="none" stroke="#1e8f2a" stroke-width="2"/><path d="M3 6l9 7 9-7" fill="none" stroke="#1e8f2a" stroke-width="2"/></svg></span>hello@tamblingardening.com</div>

  <footer class="footer">
    <div class="brand">Tamblin Gardening</div>
    <nav><span>SERVICE</span><span>ABOUT US</span><span>GALLERY</span><span>CONTACT US</span></nav>
    <span class="social" style="left:470px"></span>
    <span class="social" style="left:501px"></span>
    <span class="social" style="left:532px"></span>
  </footer>
  <div class="to-top"><svg width="10" height="10" viewBox="0 0 10 10"><path d="M5 9V1M1.5 4.5L5 1l3.5 3.5" fill="none" stroke="#1e8f2a" stroke-width="1.5"/></svg></div>
  <div class="bottom-bar"><span>© 2024 Tamblin Gardening. All rights reserved.</span><span>Terms &amp; Conditions &nbsp;|&nbsp; Privacy Policy</span></div>
</main>

<div class="board-thanks">Thanks For Watching</div>
</body>
</html>
```